Creative Brief
Corporate Image - Harborline Estate Counsel
Business Card, Envelope, Post Card, Letterhead, Email Signature
Professional
Peter J. Linwood
Managing Attorney
418 Tamsin
Cedar Hollow KS 67190
(316) 555-HOME (4663)
pl@HarborlineEstateCounsel.example
www.HarborlineEstateCounsel.example
I am planning to go with a black glossy business card so the Logo looks more striking.
In my business, judgments about how good I am are often based on how fancy my "packaging" is. The documents produced are a very important part of that "packaging."
I envision the back of the card as one large logo and then somewhere on the back (in small print) the words:
Wills, Trusts, Asset Protection, Medicaid Planning, Special Needs Planning
Here is Logo file in Black
Logo - white background - words need to be more easily readable.

```html
<!DOCTYPE html>
<html lang="en">
<head>
<meta charset="utf-8">
<title>Harborline Estate Counsel – Email Signatures</title>
<link rel="stylesheet" href="https://fonts.googleapis.com/css2?family=Tinos:wght@400;700&display=swap">
<style>
  :root {
    --stage: #e9e6e1;
    --light-bg: #ffffff;
    --light-ink: #1c1c1c;
    --light-rule: #9a9a9a;
    --dark-bg: #0b0b0b;
    --dark-bg-2: #262626;
    --dark-ink: #e6e6e6;
    --dark-rule: #6a6a6a;
  }
  * { margin: 0; padding: 0; box-sizing: border-box; }
  html, body {
    width: 1200px;
    height: 593px;
    overflow: hidden;
    background: var(--stage);
    font-family: "Tinos", "Times New Roman", serif;
  }
  .signature {
    position: absolute;
    left: 132px;
    width: 905px;
    height: 132px;
    display: flex;
    align-items: center;
    box-shadow: 0 3px 8px rgba(0,0,0,0.25);
  }
  .signature--light { top: 156px; background: var(--light-bg); color: var(--light-ink); }
  .signature--dark {
    top: 336px;
    background: linear-gradient(180deg, var(--dark-bg-2) 0%, var(--dark-bg) 100%);
    color: var(--dark-ink);
  }
  .brand {
    width: 398px;
    padding-left: 26px;
    display: flex;
    align-items: center;
    gap: 14px;
  }
  .brand-mark {
    width: 42px;
    height: 42px;
    border-radius: 50%;
    background: currentColor;
    flex: none;
  }
  .brand-name {
    font-size: 26px;
    font-weight: 400;
    letter-spacing: 0.3px;
    white-space: nowrap;
  }
  .divider {
    width: 1px;
    height: 76px;
    background: var(--light-rule);
    flex: none;
  }
  .signature--dark .divider { background: var(--dark-rule); }
  .person {
    width: 190px;
    padding-left: 34px;
  }
  .person-name { font-size: 18px; font-weight: 700; line-height: 1.2; white-space: nowrap; }
  .person-title { font-size: 15px; line-height: 1.35; white-space: nowrap; }
  .contact {
    padding-left: 12px;
    font-size: 13px;
    line-height: 18px;
    list-style: none;
    white-space: nowrap;
  }
</style>
</head>
<body>
  <section class="signature signature--light">
    <div class="brand">
      <span class="brand-mark"></span>
      <span class="brand-name">Harborline Estate Counsel</span>
    </div>
    <span class="divider"></span>
    <div class="person">
      <p class="person-name">Peter J. Linwood</p>
      <p class="person-title">Managing Attorney</p>
    </div>
    <span class="divider"></span>
    <ul class="contact">
      <li>418 Tamsin, Cedar Hollow KS 67190</li>
      <li>Phone: (316) 555-HOME (4663)</li>
      <li>Fax: (316) 555-0142</li>
      <li>Email: pl@HarborlineEstateCounsel.example</li>
      <li>www.HarborlineEstateCounsel.example</li>
    </ul>
  </section>

  <section class="signature signature--dark">
    <div class="brand">
      <span class="brand-mark"></span>
      <span class="brand-name">Harborline Estate Counsel</span>
    </div>
    <span class="divider"></span>
    <div class="person">
      <p class="person-name">Peter J. Linwood</p>
      <p class="person-title">Managing Attorney</p>
    </div>
    <span class="divider"></span>
    <ul class="contact">
      <li>418 Tamsin, Cedar Hollow KS 67190</li>
      <li>Phone: (316) 555-HOME (4663)</li>
      <li>Fax: (316) 555-0142</li>
      <li>Email: pl@HarborlineEstateCounsel.example</li>
      <li>www.HarborlineEstateCounsel.example</li>
    </ul>
  </section>
</body>
</html>
```